Business card design for web travel company

Hi
we'd like to receive some proposal for a business card design.
Stayvano is a private travel club, dedicated to all travel lovers, with unique offers for exclusive destinations all around the world. At Stayvano you can find a wide range of offers for resorts, boutique hotels and travel packages at the best guaranteed price available on the market. The convenience of the offer is guaranteed by a private sales model: offers are available for a limited time only and they are personally chosen by Stayvano's qualified team of travel experts.
We offer only exclusive hotels with discounted prices but we are not an outlet or a discount supermarket: the design should reflect our connection with luxury, exclusivity using the same style of our website www.stayvano-example.com.
We want to make sure that when we'll present ourself to our business partner they will feel immediately which is our brand positioning giving them also a sense of an affordable and reliable partner.
In attachment you can also find our brand guidelines (please note that we are NOT USING ANY MORE THE TAG LINE "Five star outlet" mentioned in it).
The info to be inserted are:
Name Surname
Job Title
Tel
Mobile (when needed)
Email
Stayvano S.r.l.
Via Bruno Lesta 27
20131 Milano

```html
<!DOCTYPE html>
<html lang="en">
<head>
<meta charset="utf-8">
<title>Stayvano – Business Card</title>
<link rel="stylesheet" href="https://fonts.googleapis.com/css2?family=Arimo:wght@400;700&display=swap">
<style>
  :root {
    --page-bg: #ffffff;
    --frame: #3a3a3a;
    --card-dark: #2b2b2b;
    --card-dark-edge: #1f1f1f;
    --card-dark-glow: #4a4a4a;
    --card-light: #ebebeb;
    --ink: #262626;
    --gold: #c9b067;
    --white: #ffffff;
  }
  * { margin: 0; padding: 0; box-sizing: border-box; }
  html, body {
    width: 1076px; height: 1200px; overflow: hidden;
    background: var(--page-bg);
    font-family: "Arimo", Arial, sans-serif;
  }
  .sheet {
    position: relative; width: 1076px; height: 1200px;
    border: 2px solid var(--frame);
  }
  .card {
    position: absolute; left: 144px; width: 781px; height: 478px;
    box-shadow: 4px 6px 14px rgba(0,0,0,0.28);
    overflow: hidden;
  }
  .card--front { top: 56px; }
  .card--back { top: 602px; background: var(--card-light); }
  .texture {
    position: absolute; inset: 0;
    background: radial-gradient(ellipse at 50% 50%, var(--card-dark-glow) 0%, var(--card-dark) 45%, var(--card-dark-edge) 100%);
  }
  .card--back .band {
    position: absolute; left: 0; top: 0; width: 100%; height: 183px;
  }
  .band .texture {
    background: radial-gradient(ellipse at 50% 40%, #3c3c3c 0%, var(--card-dark) 55%, var(--card-dark-edge) 100%);
  }
  .band-edge {
    position: absolute; left: 0; bottom: -3px; width: 100%; height: 3px;
    background: linear-gradient(90deg, transparent 5%, #bdbdbd 30%, #ffffff 50%, #bdbdbd 70%, transparent 95%);
  }
  .brand {
    position: absolute; left: 0; width: 100%; text-align: center;
    color: var(--white); font-weight: 400; letter-spacing: 1px;
    line-height: 1;
  }
  .card--front .brand { top: 246px; font-size: 84px; transform: translateY(-50%); }
  .band .brand { top: 92px; font-size: 54px; transform: translateY(-50%); }
  .person { position: absolute; left: 42px; top: 244px; color: var(--ink); }
  .person-name { font-size: 37px; font-weight: 700; line-height: 1; }
  .person-role { margin-top: 14px; margin-left: 4px; font-size: 15px; text-transform: uppercase; }
  .contact {
    position: absolute; left: 501px; top: 257px;
    font-size: 20px; color: var(--ink); line-height: 28px;
  }
  .contact dt { display: inline; color: var(--gold); font-weight: 700; margin-right: 6px; }
  .contact dd { display: inline; font-size: 18px; }
  .contact dd::after { content: ""; display: block; }
  .company { margin-top: 0; }
  .address { margin-top: 4px; line-height: 30px; }
</style>
</head>
<body>
<main class="sheet">
  <section class="card card--front">
    <div class="texture" role="img" aria-label="Dark charcoal background with fine diagonal stripe pattern"></div>
    <div class="brand">Stayvano</div>
  </section>

  <section class="card card--back">
    <header class="band">
      <div class="texture" role="img" aria-label="Dark charcoal band with fine diagonal stripe pattern"></div>
      <div class="brand">Stayvano</div>
      <div class="band-edge"></div>
    </header>

    <div class="person">
      <div class="person-name">Name Surname</div>
      <div class="person-role">Job Title</div>
    </div>

    <div class="contact">
      <dl>
        <dt>Tel</dt><dd>xxxxxxxxxxxxxx</dd>
        <dt>Mobile</dt><dd>xxxxxxxxxxxxxx</dd>
        <dt>Email</dt><dd>xxxxxxxxxxxxxx</dd>
      </dl>
      <div class="company">Stayvano S.r.l.</div>
      <address class="address" style="font-style:normal">Via Bruno Lesta 27<br>20131 Milano</address>
    </div>
  </section>
</main>
</body>
</html>
```